***PLASTIC*** Business Card Design

1 sided business card design
The card will be screen printed on plastic, so colour and fonts must be strong.

Must use the colours in the logo eps attached (Black/Ivory/White). Other colour(s) can be added.

Four (4) examples of how the logo can be printed are included in the logo eps attached.

The business card should highlight the logo. The card will be given to architects, interior designers and builders. It should look sophisticated but also innovative.

Do not cover the whole card with colour as it is important than some of the frosted plastic card is visible.

Be creative.

Target Market(s)

architects, interior designers and builders and wealthy home owners

Industry/Entity Type

Plastic

Requirements
Must have
• Must use the colours in the logo eps attached (Black/Ivory/White). Other colour(s) can be added if necessary.

The font is Square721 ExBT but has been a little thickened. It is not essential that you use this font. The name should be a stronger version of the font than other details.

The card will be printed on PVC - see http://www.voltrap.com.au/pricelistbcardsplastic.php

Final artwork must be print ready. You must use the printing spec at http://www.voltrap.com.au/2011%20PVC-TW.pdf

The actual details to be typeset ono the card are:

Dorian Welch

Mobile: 0412 806133
email: info@halcoworks.com.au
www.halcoworks.com.au

PO Box 53, Kelsbury, Vic 3027

Plastering | Rendering | Cornicing

```html
<!DOCTYPE html>
<html lang="en">
<head>
<meta charset="utf-8">
<title>Halco Works – Business Card</title>
<link rel="stylesheet" href="https://fonts.googleapis.com/css2?family=PT+Sans:wght@400;700&display=swap">
<style>
  :root {
    --page: #f4f5f6;
    --frost: #e9ebee;
    --frost-edge: #d7dadd;
    --band-dark: #1c1b1b;
    --band-light: #3b3a3a;
    --ivory: #f3e7c9;
    --white: #ffffff;
    --ink: #2a2a2a;
  }
  * { margin: 0; padding: 0; box-sizing: border-box; }
  html, body {
    width: 1200px;
    height: 767px;
    overflow: hidden;
    background: var(--page);
    font-family: "PT Sans", "Helvetica Neue", Arial, sans-serif;
  }
  .card {
    position: absolute;
    left: 306px;
    top: 110px;
    width: 663px;
    height: 378px;
    background: linear-gradient(160deg, #f0f1f3 0%, var(--frost) 60%, #e3e6e9 100%);
    border: 1px solid var(--frost-edge);
  }
  .card-layout {
    position: absolute;
    left: 328px;
    top: 285px;
    width: 622px;
    transform: skewY(-12deg);
    transform-origin: left top;
  }
  .services {
    position: absolute;
    left: 100px;
    bottom: 100%;
    margin-bottom: 4px;
    white-space: nowrap;
    color: var(--ink);
    font-size: 18px;
    letter-spacing: 2px;
  }
  .band {
    position: relative;
    height: 160px;
    background: linear-gradient(100deg, var(--band-dark) 0%, var(--band-light) 35%, var(--band-dark) 70%);
  }
  .contact {
    position: absolute;
    left: 0;
    top: 24px;
    width: 268px;
    text-align: right;
    color: var(--white);
  }
  .contact-name { font-size: 23px; line-height: 1.1; padding-right: 18px; }
  .contact-phone { font-size: 15px; line-height: 1.2; padding-right: 18px; margin-bottom: 26px; }
  .contact-line { font-size: 16px; line-height: 1.35; }
  .divider {
    position: absolute;
    left: 286px;
    top: 24px;
    width: 3px;
    height: 106px;
    background: var(--white);
  }
  .brand {
    position: absolute;
    left: 304px;
    top: 52px;
    display: flex;
    align-items: center;
    gap: 12px;
    white-space: nowrap;
    color: var(--ivory);
    font-weight: 700;
    font-size: 34px;
    letter-spacing: 2px;
    line-height: 1;
  }
  .brand-mark {
    width: 20px;
    height: 20px;
    background: var(--ivory);
  }
  .website {
    position: absolute;
    left: 310px;
    top: 100%;
    margin-top: 6px;
    white-space: nowrap;
    color: var(--ink);
    font-size: 18px;
    letter-spacing: 2.5px;
  }
</style>
</head>
<body>
  <div class="card"></div>
  <div class="card-layout">
    <p class="services">Plastering | Rendering | Cornicing</p>
    <div class="band">
      <div class="contact">
        <p class="contact-name">Dorian Welch</p>
        <p class="contact-phone">0412 806133</p>
        <p class="contact-line">PO Box 53, Kelsbury, Vic 3027</p>
        <p class="contact-line">info@halcoworks.com.au</p>
      </div>
      <div class="divider"></div>
      <div class="brand">
        <span class="brand-mark"></span>
        <span class="brand-name">HALCO WORKS</span>
      </div>
    </div>
    <p class="website">www.halcoworks.com.au</p>
  </div>
</body>
</html>
```